Kestrel Signs Facebook Banner Design

Design a facebook banner for a sign company. I would like to have a modern approach to it.

Product Offering:
Signs
Banners
Decals
Commercial Wraps

```html
<!DOCTYPE html>
<html lang="en">
<head>
<meta charset="utf-8">
<title>Kestrel Signs – Facebook Banner</title>
<link rel="stylesheet" href="https://fonts.googleapis.com/css2?family=Lato:wght@400;700&family=Lilita+One&family=Montserrat:ital,wght@0,500;0,700;0,800;1,500&family=Open+Sans:wght@600;700&display=swap">
<style>
  :root{
    --page:#ffffff;
    --red-deep:#8e0004;
    --red:#d7000a;
    --red-bright:#f0120f;
    --orange:#f58a0c;
    --amber:#f7b21a;
    --gold-tag:#d9a02a;
    --ink:#3a1a0c;
    --white:#ffffff;
    --black:#161616;
  }
  *{margin:0;padding:0;box-sizing:border-box}
  html,body{width:1200px;height:642px;overflow:hidden;background:var(--page)}
  .banner{
    position:absolute;left:173px;top:157px;width:856px;height:326px;overflow:hidden;
    background:
      radial-gradient(ellipse at 45% 40%, var(--red-bright) 0%, var(--red) 40%, var(--red-deep) 100%);
  }
  .top-glow{position:absolute;left:0;top:0;width:100%;height:12px;
    background:linear-gradient(180deg,var(--orange),rgba(245,138,12,0))}
  .rings{position:absolute;left:0;top:0}
  .bottom-band{position:absolute;left:0;top:0}
  .tagline{position:absolute;left:58px;top:63px;height:19px;padding:0 6px;
    background:var(--gold-tag);color:var(--white);
    font:400 16px/19px "Lato",sans-serif;letter-spacing:-0.2px;white-space:nowrap}
  .brand{position:absolute;left:57px;top:84px;width:272px;text-align:center;color:var(--white);
    font:800 37px/36px "Montserrat",sans-serif;letter-spacing:0.5px;text-transform:uppercase}
  .brand span{display:block;font-size:30px;line-height:34px}
  .contact{position:absolute;left:62px;top:206px;color:var(--white);font-family:"Montserrat",sans-serif}
  .contact-lead{font:italic 500 16px/20px "Montserrat",sans-serif}
  .contact-phone{font:800 19px/22px "Montserrat",sans-serif;letter-spacing:-0.6px;margin-top:2px}
  .contact-web{font:500 10.5px/14px "Montserrat",sans-serif;margin-top:1px}
  .services-title{position:absolute;left:321px;top:136px;width:138px;height:22px;background:var(--white);
    color:var(--red);text-align:center;font:700 17px/22px "Open Sans",sans-serif;letter-spacing:0.2px}
  .services-list{position:absolute;left:200px;top:161px;width:259px;list-style:none;text-align:right;
    color:var(--white);font:600 19.5px/24px "Open Sans",sans-serif;letter-spacing:-0.3px}
  .services-list li::after{content:"‹";font-weight:700;margin-left:6px}
  .pointer{position:absolute;left:304px;top:180px}
  .headline{position:absolute;left:488px;top:78px;width:290px;font-family:"Lilita One",sans-serif;
    text-transform:uppercase;text-align:center}
  .headline span{display:block;background:linear-gradient(180deg,var(--amber) 10%,var(--orange) 70%,#e2470a);
    -webkit-background-clip:text;background-clip:text;color:transparent;
    -webkit-text-stroke:1.5px var(--ink);filter:drop-shadow(2px 3px 0 var(--ink))}
  .headline-design{font-size:40px;line-height:42px;text-align:left;padding-left:10px;letter-spacing:-1px}
  .headline-print{font-size:90px;line-height:84px;letter-spacing:-2px}
  .headline-install{font-size:52px;line-height:50px;letter-spacing:-1px;padding-left:50px}
  .social{position:absolute;left:809px;top:26px;list-style:none}
  .social li{width:14px;height:14px;border:2px solid var(--white);border-radius:50%;margin-bottom:4.5px}
  .social-rule{position:absolute;left:827px;top:0;width:1px;height:99px;background:var(--white)}
  .order-btn{position:absolute;left:716px;top:275px;height:25px;display:flex;border-radius:3px;overflow:hidden;
    font:800 12.5px/25px "Montserrat",sans-serif;letter-spacing:0.4px}
  .order-btn-label{background:var(--white);color:var(--black);padding:0 5px 0 7px}
  .order-btn-icon{background:var(--black);width:20px;display:flex;align-items:center;justify-content:center}
</style>
</head>
<body>
<main class="banner">
  <div class="top-glow"></div>

  <svg class="rings" width="856" height="326" viewBox="0 0 856 326" aria-hidden="true">
    <defs>
      <linearGradient id="ringOuter" x1="0" y1="0" x2="1" y2="1">
        <stop offset="0" stop-color="#f7a21a"/><stop offset="1" stop-color="#e96b0b"/>
      </linearGradient>
      <linearGradient id="ringInner" x1="0" y1="0" x2="1" y2="1">
        <stop offset="0" stop-color="#f08010"/><stop offset="1" stop-color="#f7b31a"/>
      </linearGradient>
    </defs>
    <circle cx="612" cy="205" r="175" fill="none" stroke="url(#ringOuter)" stroke-width="42" opacity="0.92"/>
    <circle cx="612" cy="205" r="118" fill="none" stroke="url(#ringInner)" stroke-width="28" opacity="0.85"/>
  </svg>

  <svg class="bottom-band" width="856" height="326" viewBox="0 0 856 326" aria-hidden="true">
    <defs>
      <linearGradient id="band" x1="0" y1="0" x2="0" y2="1">
        <stop offset="0" stop-color="#f39a0f"/><stop offset="1" stop-color="#e7830a"/>
      </linearGradient>
    </defs>
    <path d="M0 285 C200 272 500 262 700 272 C780 276 830 280 846 284 L846 326 L0 326 Z" fill="url(#band)"/>
  </svg>

  <p class="tagline">TRANSFORM YOUR BRAND WITH</p>
  <h1 class="brand">Kestrel<span>Signs</span></h1>

  <div class="contact">
    <p class="contact-lead">Call us Now:</p>
    <p class="contact-phone">+1 555-014-2290</p>
    <p class="contact-web">WWW.KESTRELSIGNS.CA</p>
  </div>

  <h2 class="services-title">OUR SERVICES</h2>
  <ul class="services-list">
    <li>Signs</li>
    <li>Banners</li>
    <li>Decals</li>
    <li>Commercial Wraps</li>
  </ul>
  <svg class="pointer" width="50" height="50" viewBox="0 0 50 50" aria-hidden="true">
    <path d="M4 46 L40 10 M26 6 L44 4 L42 22" fill="none" stroke="#fff" stroke-width="2.2" stroke-linecap="round" stroke-linejoin="round"/>
    <path d="M2 42 L36 8 M8 48 L42 14" fill="none" stroke="#fff" stroke-width="1.4" stroke-linecap="round"/>
  </svg>

  <div class="headline">
    <span class="headline-design">Design</span>
    <span class="headline-print">Print</span>
    <span class="headline-install">Install</span>
  </div>

  <div class="social-rule"></div>
  <ul class="social" aria-label="Social links">
    <li></li><li></li><li></li><li></li>
  </ul>

  <div class="order-btn">
    <span class="order-btn-label">ORDER NOW</span>
    <span class="order-btn-icon">
      <svg width="11" height="11" viewBox="0 0 11 11" aria-hidden="true">
        <path d="M1 5.5 H9 M5.5 2 L9 5.5 L5.5 9" fill="none" stroke="#fff" stroke-width="1.6" stroke-linecap="round" stroke-linejoin="round"/>
      </svg>
    </span>
  </div>
</main>
</body>
</html>
```